Lanterne architecture business cards

We are a new company based in New Zealand. We Specialize in High end Luxury Residential Architecture.

Every home is bespoke and is designed to each clients individual requirements and needs.

I like to design buildings that inspire people through light and form while offering a high level of comfort and usability.

Lines of sight, proportion and balance are fundamental to the spaces I create.
Updates

August 5th is current deadline - Today's date is the 13th of August.

Target Market(s)

New Zealanders who want a custom individual home design, typically 30-65 year old males and females

Industry/Entity Type

Architecture

Contact Information for Business Card

Director - Derek Tolson
Contact Number - 0279164073
Email - info@lanternearchitecture-example.co.nz
Webstie - www.lanternearchitecture-example.co.nz
Social Media - @lanternearchitecture

Font styles to use
Sans Serif

Requirements
Must have
• Logo (Both Sides)
Website
Email
Contact Number
Social Media

Nice to have
• Texture
Should not have
• More than 3 colours - typically I would've thought 2 would be good to match the logo.

```html
<!DOCTYPE html>
<html lang="en">
<head>
<meta charset="utf-8">
<title>Lanterne architecture business cards</title>
<link rel="stylesheet" href="https://fonts.googleapis.com/css2?family=Jost:wght@300;400;500&display=swap">
<style>
  :root {
    --backdrop: #b3b4b6;
    --paper: #e9e9e7;
    --paper-shade: #dcdcda;
    --ink: #2b2b2b;
    --ink-soft: #6d6d6d;
    --edge: #1f1f1f;
  }
  * { margin: 0; padding: 0; box-sizing: border-box; }
  html, body {
    width: 1200px; height: 966px; overflow: hidden;
    background: var(--backdrop);
    font-family: "Jost", sans-serif;
    color: var(--ink);
  }
  .sheet {
    width: 1200px; height: 966px;
    display: flex; align-items: center; justify-content: center; gap: 40px;
  }
  .card {
    position: relative;
    width: 540px; height: 310px;
    background: var(--paper);
    border-bottom: 3px solid var(--edge);
  }
  /* Front */
  .brand { position: absolute; left: 64px; top: 58px; }
  .brand-name {
    font-size: 30px; font-weight: 400; letter-spacing: 12px;
    text-transform: uppercase; color: var(--ink); line-height: 1;
  }
  .brand-sub {
    margin-top: 6px; font-size: 10px; font-weight: 400;
    letter-spacing: 9.5px; text-transform: uppercase; color: var(--ink);
  }
  .social {
    position: absolute; left: 34px; top: 186px;
    font-size: 14px; font-weight: 300; color: var(--ink-soft);
  }
  .person { position: absolute; left: 282px; top: 176px; }
  .person-name {
    font-size: 16px; font-weight: 500; letter-spacing: 2px;
    text-transform: uppercase; color: var(--ink);
  }
  .person-role { font-size: 13px; font-weight: 300; color: var(--ink-soft); }
  .contacts {
    position: absolute; left: 282px; top: 232px;
    list-style: none; font-size: 12px; font-weight: 300; color: var(--ink-soft);
  }
  .contacts li { display: flex; align-items: center; gap: 7px; line-height: 18px; }
  .contacts svg { width: 10px; height: 10px; fill: var(--ink); flex: none; }
  /* Back */
  .card-back { display: flex; align-items: center; justify-content: center; }
  .texture {
    position: absolute; inset: 0;
    background: radial-gradient(ellipse at 50% 50%, var(--paper) 0%, var(--paper-shade) 55%, var(--paper) 100%);
  }
  .back-mark {
    position: relative;
    font-size: 34px; font-weight: 400; letter-spacing: 12px;
    text-transform: uppercase; color: var(--ink);
  }
</style>
</head>
<body>
<main class="sheet">
  <section class="card card-front">
    <div class="brand">
      <div class="brand-name">Lanterne</div>
      <div class="brand-sub">architecture</div>
    </div>
    <p class="social">@lanternearchitecture</p>
    <div class="person">
      <p class="person-name">Derek Tolson</p>
      <p class="person-role">Director</p>
    </div>
    <ul class="contacts">
      <li>
        <svg viewBox="0 0 10 10" aria-hidden="true"><path d="M2 0.5 L3.6 2.8 L2.7 3.8 Q3.6 5.8 5.9 7.2 L6.9 6.3 L9.5 7.8 L8.4 9.5 Q4 9 1.4 5.2 Q0.4 3.2 0.6 1.6 Z"/></svg>
        0279164073
      </li>
      <li>
        <svg viewBox="0 0 10 10" aria-hidden="true"><path d="M0 2 H10 V8.5 H0 Z M0.8 2.6 L5 5.8 L9.2 2.6" fill="none" stroke="#2b2b2b" stroke-width="1.1"/></svg>
        info@lanternearchitecture-example.co.nz
      </li>
      <li>
        <svg viewBox="0 0 10 10" aria-hidden="true"><circle cx="5" cy="5" r="4.4" fill="none" stroke="#2b2b2b" stroke-width="1"/><path d="M0.6 5 H9.4 M5 0.6 V9.4 M5 0.6 Q2 5 5 9.4 M5 0.6 Q8 5 5 9.4" fill="none" stroke="#2b2b2b" stroke-width="0.8"/></svg>
        www.lanternearchitecture-example.co.nz
      </li>
    </ul>
  </section>

  <section class="card card-back">
    <div class="texture" role="img" aria-label="Embossed pattern of fine concentric lines radiating around the centre"></div>
    <div class="back-mark">Lanterne</div>
  </section>
</main>
</body>
</html>
```